Documentary filmmaker needs a movie poster for a film that will screen in an upcoming festival

I am a documentary filmmaker who has recently had a film accepted to screen in a film festival. The film is called "A Lantern at Dusk" and the film synopsis is:
A single, working mother in the heart of the Mississippi Delta sees hard work, education and faith as the foundation for raising her three high school daughters. She is neither a hero nor a victim of society, but rather a simple, hardworking woman who puts one foot in front of the other each day with lantern at dusk.
I have some photo stills that I took from the film. I am looking for a movie poster that communicates the idea of "lantern at dusk". I also want to it to somehow communicate the setting - deep south, small town, lower socio-economic group while respecting the main character as neither a victim or a hero. But a solid, dependable, humble woman.
I can provide a link to view the 18 min documentary to get a better sense of the film.
Reason: Extended deadline by 3 days in order to get an image uploaded. Still having trouble doing this! If anyone has any suggestions, please give them to me.
I have posted a still from the film. If anyone wants to view it, I think it is viewable now. I had a special character in the name earlier and it seemed to cause problems.
I have added a still image from the film that could help. It could either be used (if quality permits) or be looked at to guide thinking about feel and tone of film.

```html
<!DOCTYPE html>
<html lang="en">
<head>
<meta charset="utf-8">
<title>A Lantern at Dusk — Film Poster</title>
<link rel="stylesheet" href="https://fonts.googleapis.com/css2?family=Bebas+Neue&family=Oswald:wght@400;700&display=swap">
<style>
  :root {
    --canvas-bg: #000000;
    --poster-bg: #000000;
    --poster-border: #ffffff;
    --photo-dark: #000000;
    --photo-mid: #2b2b2b;
    --photo-light: #ffffff;
    --tagline: #e07a2a;
    --title: #8ec0e8;
    --name: #4a4a4a;
    --credit: #3a3a3a;
  }
  html, body {
    margin: 0;
    padding: 0;
    width: 1200px;
    height: 1000px;
    overflow: hidden;
    background: var(--canvas-bg);
  }
  .canvas {
    position: relative;
    width: 1200px;
    height: 1000px;
  }
  .poster {
    position: absolute;
    left: 395px;
    top: 191px;
    width: 407px;
    height: 618px;
    border: 2px solid var(--poster-border);
    background: var(--poster-bg);
    overflow: hidden;
  }
  .photo-still {
    position: absolute;
    left: 0;
    top: 0;
    width: 407px;
    height: 618px;
  }
  .tagline {
    position: absolute;
    right: 15px;
    top: 17px;
    margin: 0;
    text-align: right;
    font-family: "Bebas Neue", sans-serif;
    font-size: 33px;
    line-height: 29px;
    letter-spacing: 2px;
    color: var(--tagline);
  }
  .lead-name {
    position: absolute;
    left: 0;
    width: 407px;
    top: 381px;
    text-align: center;
    font-family: "Oswald", sans-serif;
    font-weight: 700;
    font-size: 13px;
    letter-spacing: 0.2px;
    color: var(--name);
    transform: translateX(-5px) scaleY(1.15);
  }
  .title {
    position: absolute;
    left: 0;
    width: 407px;
    top: 404px;
    margin: 0;
    font-family: "Bebas Neue", sans-serif;
    font-weight: 400;
    color: var(--title);
    text-align: center;
  }
  .title-small {
    display: block;
    font-size: 50px;
    line-height: 50px;
    transform: translateX(2px);
  }
  .title-large {
    display: block;
    font-size: 132px;
    line-height: 112px;
    letter-spacing: 2px;
  }
  .credits {
    position: absolute;
    left: 10px;
    right: 6px;
    top: 557px;
    font-family: "Oswald", sans-serif;
    color: var(--credit);
    font-size: 6px;
    line-height: 15px;
    white-space: nowrap;
  }
  .credit-line { margin: 0; }
  .credit-role { font-style: italic; font-weight: 700; margin-right: 6px; }
  .credit-line b { font-size: 9px; font-weight: 700; margin-right: 3px; }
</style>
</head>
<body>
<div class="canvas">
  <section class="poster">
    <svg class="photo-still" viewBox="0 0 407 618" role="img" aria-label="Photo still from the film: the main subject, a woman in glasses and a white shirt, looking upward against a dark background">
      <defs>
        <linearGradient id="photoTone" x1="0.7" y1="0" x2="0.3" y2="1">
          <stop offset="0" stop-color="var(--photo-dark)"/>
          <stop offset="0.35" stop-color="var(--photo-mid)"/>
          <stop offset="0.62" stop-color="var(--photo-light)"/>
          <stop offset="1" stop-color="var(--photo-light)"/>
        </linearGradient>
      </defs>
      <rect x="0" y="0" width="407" height="618" fill="url(#photoTone)"/>
    </svg>

    <p class="tagline">Hard Work<br>Education<br>Faith</p>

    <div class="lead-name">LORETTA VANCE</div>

    <h1 class="title">
      <span class="title-small">A Lantern</span>
      <span class="title-large">At Dusk</span>
    </h1>

    <div class="credits">
      <p class="credit-line"><span class="credit-role">A FILM BY</span>MILES <b>HARLAN</b> CLARA <b>BENEDETTI</b> RUTH <b>ELLISON</b> MATTEO <b>RICARDI</b></p>
      <p class="credit-line"><span class="credit-role">INSTRUCTED &amp; PRODUCED BY</span>NORA <b>CASTELLANO</b> WESLEY <b>PORTER</b></p>
      <p class="credit-line"><span class="credit-role">FEATURING</span>JUNE <b>VANCE</b> TESSA <b>VANCE</b> MARLA <b>VANCE</b> IDA <b>BROOKS</b> RIVERBEND HIGH SCHOOL <b>BAND</b> KEISHA <b>LOWE</b> DANA <b>BROOKS</b></p>
    </div>
  </section>
</div>
</body>
</html>
```